Online Marketing Agency Website

We are an online marketing agency that specializes in search marketing (SEM) for businesses of all sizes. Our core services include local search marketing, seo, paid search, paid social, graphic design, video production/editing and website design. We have an existing website that we launched a number of years ago but it's very outdated and we're currently too busy to design a new version.

Target Market(s)

Any business that needs online marketing services with an emphasis on search marketing.

Industry/Entity Type

Ad Agency

Number of Pages Required

4 page

Font styles to use
Sans Serif

Requirements
Must have
• Home page, interior page, blog page, contact us page.
Look and feel should be modern and clean and easy to navigate.
Sections for call outs for specific services: Business Marketing Strategy, Content Creation and Marketing, Graphic & Publication Design, Pay Per Click (PPC) Management, Search Engine Optimization, Social Media Management, Video Production & Editing, Website Hosting & Management, Website Design & Development
Use color from logo that was uploaded.

```html
<!DOCTYPE html>
<html lang="en">
<head>
<meta charset="utf-8">
<title>Lift Digital – Services</title>
<link href="https://fonts.googleapis.com/css2?family=Hind:wght@700&family=Open+Sans:wght@400;600;700&display=swap" rel="stylesheet">
<style>
:root{
  --ink:#0d3b4f;
  --text:#2b4a5a;
  --muted:#7a7a7a;
  --accent:#ff4400;
  --band:#ececec;
  --line:#cfd3d6;
  --white:#ffffff;
  --cyan:#8ef4f7;
}
*{box-sizing:border-box;margin:0;padding:0}
html,body{width:1200px;height:3189px;overflow:hidden}
body{position:relative;background:var(--white);font-family:"Open Sans",Arial,sans-serif;color:var(--text)}
.abs{position:absolute}
.hero-visual{left:372px;top:0;width:828px;height:483px;
  background:linear-gradient(110deg,#f4f1ec 0%,#e9e2d8 35%,#9c8a7c 62%,#6d5b52 75%,#d9d3cc 90%);
  -webkit-mask-image:radial-gradient(ellipse 70% 75% at 60% 35%,#000 40%,transparent 100%);
  mask-image:radial-gradient(ellipse 70% 75% at 60% 35%,#000 40%,transparent 100%);opacity:.75}
.brand{left:120px;top:84px;font-size:16px;font-weight:600;color:var(--ink);letter-spacing:.3px;display:flex;align-items:center;gap:8px}
.brand-dot{width:14px;height:14px;border-radius:50%;background:var(--accent)}
.nav{top:52px;left:0;width:1200px}
.nav a{position:absolute;font-size:15px;color:#222;text-decoration:none}
.hero-title{top:228px;left:0;width:1215px;text-align:center;font-family:"Hind",Arial,sans-serif;font-weight:700;font-size:47px;line-height:50px;color:var(--ink)}
.hero-sub{top:334px;left:0;width:1215px;text-align:center;font-size:19px;font-weight:400;color:var(--muted)}
.section-title{left:0;width:1212px;text-align:center;font-size:33px;font-weight:600;color:var(--ink)}
.band{left:0;top:1040px;width:1200px;height:614px;background:var(--band)}
.card{display:flex;flex-direction:column;align-items:center;text-align:center}
.card.raised{background:var(--white);border-radius:6px;box-shadow:0 4px 18px rgba(0,0,0,.08)}
.card-art{margin-top:52px;width:186px;height:152px;border-radius:10px;
  background:linear-gradient(135deg,rgba(255,68,0,.18),rgba(142,244,247,.35))}
.card-label{margin-top:58px;font-size:21px;line-height:25px;color:var(--ink)}
.touch-title{left:430px;top:2352px;font-family:"Hind",Arial,sans-serif;font-weight:700;font-size:48px;color:var(--ink)}
.info h3{font-size:22px;font-weight:700;color:var(--ink)}
.info p{font-size:16px;line-height:31px;color:var(--text)}
.field{border:1px solid var(--line);border-radius:3px;background:var(--white);font-size:12px;color:#8a8a8a;padding:14px 18px}
.captcha{left:431px;top:2836px;width:266px;height:66px;border:1px solid #d3d3d3;border-radius:3px;background:#f9f9f9;display:flex;align-items:center;padding-left:12px;gap:10px;font-size:12px;color:#333}
.captcha-box{width:24px;height:24px;border:2px solid #c1c1c1;border-radius:2px;background:var(--white)}
.captcha-mark{position:absolute;right:14px;top:16px;width:28px;height:28px;border-radius:4px;background:#c9d3e6}
.send{left:431px;top:2929px;width:132px;height:43px;background:var(--accent);border-radius:4px;color:var(--white);font-size:14px;font-weight:700;display:flex;align-items:center;justify-content:center}
.footer{left:0;top:3102px;width:1200px;height:87px;background:var(--accent);color:var(--white);font-size:16px;padding:33px 0 0 116px}
</style>
</head>
<body>
<div class="abs hero-visual" role="img" aria-label="Blurred photo of a person working in an office with bookshelves"></div>

<div class="abs brand"><span class="brand-dot"></span>LIFT DIGITAL</div>
<nav class="abs nav">
  <a style="left:669px">HOME</a>
  <a style="left:763px">SERVICES</a>
  <a style="left:890px">BLOG</a>
  <a style="left:985px">CONTACT</a>
</nav>

<h1 class="abs hero-title">LET’S GROW<br>YOUR BUSINESS</h1>
<p class="abs hero-sub">- Our Services -</p>

<h2 class="abs section-title" style="top:526px">Strategy</h2>
<div class="abs card raised" style="left:290px;top:615px;width:307px;height:334px">
  <div class="card-art" role="img" aria-label="Chess knight and pawns icon"></div>
  <div class="card-label">Business Marketing<br>Strategy</div>
</div>
<div class="abs card" style="left:616px;top:615px;width:307px;height:334px">
  <div class="card-art" role="img" aria-label="Play button on screen icon"></div>
  <div class="card-label">Pay Per Click (PPC)<br>Management</div>
</div>

<div class="abs band"></div>
<h2 class="abs section-title" style="top:1106px">Content</h2>
<div class="abs card raised" style="left:126px;top:1185px;width:309px;height:333px">
  <div class="card-art" role="img" aria-label="Chess knight and pawns icon"></div>
  <div class="card-label">Content Creation<br>and Marketing</div>
</div>
<div class="abs card raised" style="left:453px;top:1185px;width:307px;height:333px">
  <div class="card-art" role="img" aria-label="Play button on screen icon"></div>
  <div class="card-label">Graphic &amp; Publication<br>Design</div>
</div>
<div class="abs card raised" style="left:778px;top:1185px;width:315px;height:333px">
  <div class="card-art" role="img" aria-label="Magnifier and bar chart icon"></div>
  <div class="card-label">Video Production<br>&amp; Editing</div>
</div>

<h2 class="abs section-title" style="top:1720px">Optimization</h2>
<div class="abs card raised" style="left:290px;top:1809px;width:307px;height:332px">
  <div class="card-art" role="img" aria-label="Chess knight and pawns icon"></div>
  <div class="card-label">Search Engine<br>Optimization</div>
</div>
<div class="abs card" style="left:616px;top:1809px;width:307px;height:332px">
  <div class="card-art" role="img" aria-label="Play button on screen icon"></div>
  <div class="card-label">Website Design &amp;<br>Development</div>
</div>

<h2 class="abs touch-title">GET IN TOUCH</h2>
<div class="abs info" style="left:116px;top:2438px">
  <h3>Lift Digital</h3>
  <p style="margin-top:8px">Harbor Street 12, Lakeview<br>Canada</p>
  <h3 style="margin-top:38px">Office Hours</h3>
  <p style="margin-top:2px">Monday - Friday<br>08.00 am - 16.00 pm</p>
  <h3 style="margin-top:38px">Email Support</h3>
  <p style="margin-top:2px">support@liftdigital.example</p>
</div>

<div class="abs field" style="left:431px;top:2443px;width:326px;height:44px">Name*</div>
<div class="abs field" style="left:774px;top:2443px;width:324px;height:44px">Company*</div>
<div class="abs field" style="left:431px;top:2514px;width:326px;height:44px">Email*</div>
<div class="abs field" style="left:774px;top:2514px;width:324px;height:44px">Services</div>
<div class="abs field" style="left:431px;top:2584px;width:667px;height:44px">Subject*</div>
<div class="abs field" style="left:431px;top:2655px;width:667px;height:157px">Messages*</div>
<div class="abs captcha"><span class="captcha-box"></span>I'm not a robot<span class="captcha-mark"></span></div>
<div class="abs send">SEND!</div>

<footer class="abs footer">Lift Digital Copyright © 2020</footer>
</body>
</html>
```